Business Card Design

We need a cool business card for a new Beer Pong events and table sales company. We want it to be bright and fun. Maybe even have a table design on one side. Be creative and outgoing with it.

**I have attached a file that I have done as a potential idea, please think about it while designing**

Target Market(s)

18-40 year olds interested in playing drinking games

Industry/Entity Type

Events

Contact Information for Business Card

Harbourline Cup Toss
info@harbourlinecuptoss.com.au
www.harbourlinecuptoss.com.au
www.facebook.com/harbourlinecuptoss
www.twitter.com/harbourtoss

Font styles to use
Other font styles liked:
• College style font like in my file

```html
<!DOCTYPE html>
<html lang="en">
<head>
<meta charset="utf-8">
<title>Harbourline Cup Toss – Business Card</title>
<link rel="stylesheet" href="https://fonts.googleapis.com/css2?family=Krona+One&family=Michroma&display=swap">
<style>
  :root {
    --backdrop: #d9d9d9;
    --card-white: #ffffff;
    --card-black: #0b0b0b;
    --ink: #111111;
    --ink-soft: #3a3a3a;
    --rule: #8a8a8a;
    --accent: #e8262d;
  }
  * { box-sizing: border-box; margin: 0; padding: 0; }
  html, body {
    width: 1200px;
    height: 750px;
    overflow: hidden;
  }
  body {
    background: var(--backdrop);
    display: flex;
    align-items: center;
    justify-content: center;
    gap: 40px;
  }
  .card {
    position: relative;
    width: 540px;
    height: 309px;
    border-radius: 26px;
    overflow: hidden;
  }

  /* Shared brand mark */
  .brand-mark {
    display: flex;
    align-items: center;
    gap: 8px;
  }
  .brand-mark .mark-square {
    flex: none;
    width: 14px;
    height: 14px;
    background: var(--accent);
  }
  .brand-mark .mark-name {
    font-family: "Krona One", sans-serif;
    font-size: 10px;
    color: var(--ink);
    text-transform: uppercase;
    white-space: nowrap;
  }

  /* Front */
  .card-front { background: var(--card-white); color: var(--ink); }
  .card-front .brand-mark {
    position: absolute;
    top: 58px;
    left: 0;
    right: 0;
    justify-content: center;
    padding-left: 110px;
  }
  .card-front .company-name {
    position: absolute;
    top: 124px;
    left: 0;
    right: 0;
    text-align: center;
    padding-left: 50px;
    font-family: "Krona One", sans-serif;
    font-size: 21px;
    font-weight: 400;
    letter-spacing: 0.5px;
    text-transform: uppercase;
    white-space: nowrap;
  }
  .contact-list {
    position: absolute;
    left: 30px;
    bottom: 34px;
    list-style: none;
    border-left: 1.5px solid var(--rule);
    padding-left: 8px;
    font-family: "Michroma", sans-serif;
    font-size: 8.5px;
    line-height: 1.45;
    color: var(--ink-soft);
    text-transform: uppercase;
  }

  /* Back */
  .card-back { background: var(--card-black); }
  .card-back .cup-dots {
    position: absolute;
    inset: 0;
    width: 100%;
    height: 100%;
  }
  .center-disc {
    position: absolute;
    left: 165px;
    top: 30px;
    width: 250px;
    height: 250px;
    border-radius: 50%;
    background: var(--card-white);
    display: flex;
    flex-direction: column;
    align-items: center;
    justify-content: center;
    gap: 20px;
  }
  .center-disc .company-name {
    font-family: "Krona One", sans-serif;
    font-size: 11.5px;
    font-weight: 400;
    color: var(--ink);
    text-transform: uppercase;
    white-space: nowrap;
  }
</style>
</head>
<body>

  <section class="card card-front" aria-label="Business card front">
    <div class="brand-mark">
      <span class="mark-square"></span>
      <span class="mark-name">Harbourline Cup Toss</span>
    </div>
    <h1 class="company-name">Harbourline Cup Toss</h1>
    <ul class="contact-list">
      <li>info@harbourlinecuptoss.com.au</li>
      <li>www.harbourlinecuptoss.com.au</li>
      <li>www.facebook.com/harbourlinecuptoss</li>
      <li>www.twitter.com/harbourtoss</li>
    </ul>
  </section>

  <section class="card card-back" aria-label="Business card back">
    <svg class="cup-dots" viewBox="0 0 540 309" aria-hidden="true">
      <g fill="#ffffff">
        <circle cx="70" cy="72" r="12"/>
        <circle cx="98" cy="198" r="12"/>
        <circle cx="190" cy="276" r="12"/>
        <circle cx="402" cy="36" r="12"/>
        <circle cx="458" cy="110" r="12"/>
        <circle cx="484" cy="214" r="12"/>
      </g>
    </svg>
    <div class="center-disc">
      <div class="brand-mark">
        <span class="mark-square"></span>
        <span class="mark-name">Harbourline Cup Toss</span>
      </div>
      <h2 class="company-name">Harbourline Cup Toss</h2>
    </div>
  </section>

</body>
</html>
```